Skip Bin Hire Business

We are an existing business that hire out skip bins for domestic and commercial use. We are looking for a fresh look with no colours or designs in mind.
We have 2m3 and 3m3 skip bins and 3m3 up to 24m3 walk in bins.
Visit our website for more information.
www.harborcrate.com.au
We are going to add a photo of a 3m3 skip as this is a new product for our company and not available on our website at this stage.

Industry/Entity Type

Business

Contact Information for Business Card

Harbor Crate
9172-4086
www.harborcrate.com.au

```html
<!DOCTYPE html>
<html lang="en">
<head>
<meta charset="utf-8">
<title>Harbor Crate – Business Card</title>
<link rel="stylesheet" href="https://fonts.googleapis.com/css2?family=Archivo+Black&family=Open+Sans:wght@400;600&display=swap">
<style>
  :root {
    --backdrop: #ecebe8;
    --sun-light: #f2c62a;
    --sun-mid: #e9b41c;
    --sun-deep: #e08e10;
    --band-white: #f7f7f5;
    --steel-light: #d4d4d4;
    --steel-dark: #a9a9a9;
    --crate-light: #d9a431;
    --crate-dark: #a8761a;
    --ink: #2a2208;
    --paper: #ffffff;
  }
  html, body {
    margin: 0;
    width: 1200px;
    height: 723px;
    overflow: hidden;
    background: var(--backdrop);
  }
  .stage {
    position: relative;
    width: 1200px;
    height: 723px;
  }
  .business-card {
    position: absolute;
    left: 420px;
    top: 82px;
    width: 360px;
    height: 560px;
    filter: drop-shadow(0 10px 24px rgba(0,0,0,0.18));
  }
  .brand-name {
    font-family: "Archivo Black", "Arial Black", sans-serif;
    font-size: 74px;
    fill: var(--paper);
    letter-spacing: -1px;
  }
  .contact-line {
    font-family: "Open Sans", Arial, sans-serif;
    font-size: 12px;
    fill: var(--ink);
  }
  .tagline {
    font-family: "Open Sans", Arial, sans-serif;
    font-size: 15px;
    fill: var(--paper);
    letter-spacing: 0.4px;
  }
</style>
</head>
<body>
<main class="stage">
  <svg class="business-card" viewBox="0 0 360 560" xmlns="http://www.w3.org/2000/svg" aria-label="Harbor Crate business card">
    <defs>
      <clipPath id="card-shape">
        <rect x="0" y="0" width="360" height="560" rx="34" ry="34"/>
      </clipPath>
      <linearGradient id="sun-fill" x1="0" y1="0" x2="1" y2="0.6">
        <stop offset="0" stop-color="var(--sun-light)"/>
        <stop offset="0.55" stop-color="var(--sun-mid)"/>
        <stop offset="1" stop-color="var(--sun-deep)"/>
      </linearGradient>
      <linearGradient id="steel-fill" x1="0" y1="0" x2="1" y2="1">
        <stop offset="0" stop-color="var(--steel-light)"/>
        <stop offset="1" stop-color="var(--steel-dark)"/>
      </linearGradient>
      <linearGradient id="crate-fill" x1="0" y1="0" x2="1" y2="1">
        <stop offset="0" stop-color="var(--crate-light)"/>
        <stop offset="1" stop-color="var(--crate-dark)"/>
      </linearGradient>
    </defs>

    <g clip-path="url(#card-shape)">
      <rect class="card-base" x="0" y="0" width="360" height="560" fill="url(#sun-fill)"/>

      <polygon class="white-band" points="0,318 360,222 360,252 0,342" fill="var(--band-white)"/>
      <polygon class="steel-panel" points="28,340 360,254 360,560 150,560" fill="url(#steel-fill)"/>

      <polygon class="product-photo" role="img" aria-label="Photo of stacked yellow skip bins labelled commercial and residential"
               points="108,478 360,400 360,560 168,560" fill="url(#crate-fill)"/>
    </g>

    <text class="tagline tagline-lead" transform="translate(112,470) rotate(-17.2)">What Waste Can You Put</text>
    <text class="tagline tagline-tail" transform="translate(322,388) rotate(76)">In Our Skip Bins</text>

    <text class="brand-name" x="16" y="78">Harbor</text>
    <text class="brand-name" x="16" y="152">Crate</text>

    <text class="contact-line" x="18" y="182">phone:<tspan x="62">(03) 9172 4086</tspan></text>
    <text class="contact-line" x="18" y="199">www.harborcrate.com.au</text>
  </svg>
</main>
</body>
</html>
```